A modern, fresh introduction to Buddhism

I need a book cover for an A6 sized book to be used both for ebook and hard copy. The author is a young, modern Buddhist teacher of high standing who has written this short intro to Buddhism in an informal Q & As format using modern, accessible language to convey profound and meaningful ideas to the general public. The author is Tibetan, but teaches worldwide and is very personable and dynamic. The cover should portray this and have a fresh yet authentic feel to it (nothing new-agey!). Please see the author's websites www.norvalemtasheteacher.org and www.pwrt.org for reference, but do not feel that the design must align completely with the website designs.

Target Market(s)

General public both in Europe and America and in Asia ranging from teenagers to the elderly. A really broad audience.

Industry/Entity Type

Teacher

Requirements
Must have
• Please include the following text that on the front cover:

A Window onto Stillness

By Drawa Tsomen Lhundrup

Please include the following on the back cover:

Yunor Trenpa Publications (with attached logo above it)
Nice to have
• A simplistic, artistic, and modern look without any traditional religious images.
Should not have
• No buddha images or religious images. I would prefer a more simplistic, modern and artistic look.

```html
<!DOCTYPE html>
<html lang="en">
<head>
<meta charset="utf-8">
<title>A Window onto Stillness – Cover Spread</title>
<link rel="stylesheet" href="https://fonts.googleapis.com/css2?family=Roboto:wght@300;500;700&display=swap">
<style>
  :root {
    --maroon: #6a1a30;
    --glow-core: #e06b3c;
    --glow-mid: #a8443a;
    --saffron: #e8891e;
    --rule-dark: #4e1418;
    --ink-light: #f3e6ea;
    --white: #ffffff;
    --page: #ffffff;
  }
  html, body {
    margin: 0;
    padding: 0;
    width: 1200px;
    height: 900px;
    overflow: hidden;
    background: var(--page);
    font-family: "Roboto", Arial, sans-serif;
  }
  .canvas {
    position: relative;
    width: 1200px;
    height: 900px;
  }
  .cover-spread {
    position: absolute;
    left: 90px;
    top: 110px;
    width: 1020px;
    height: 680px;
    overflow: hidden;
    background:
      radial-gradient(ellipse 430px 420px at 510px 680px,
        var(--glow-core) 0%, var(--glow-mid) 45%, var(--maroon) 100%);
  }
  .spine-fold {
    position: absolute;
    top: 0;
    bottom: 0;
    width: 1px;
    background: rgba(255, 255, 255, 0.08);
  }
  .spine-fold--left { left: 482px; }
  .spine-fold--right { left: 538px; }

  .spine-title {
    position: absolute;
    left: 510px;
    top: 97px;
    transform-origin: 0 0;
    transform: rotate(90deg) translateY(-50%);
    color: var(--ink-light);
    font-weight: 300;
    font-size: 14px;
    letter-spacing: 1.8px;
    white-space: nowrap;
    text-transform: uppercase;
  }

  .publisher {
    position: absolute;
    left: 0;
    width: 482px;
    top: 98px;
    text-align: center;
  }
  .publisher-mark {
    display: block;
    width: 98px;
    height: 98px;
    margin: 0 auto 24px;
    border: 1px solid var(--ink-light);
    border-radius: 50%;
    box-sizing: border-box;
  }
  .publisher-name {
    color: var(--ink-light);
    font-weight: 300;
    font-size: 16px;
    letter-spacing: 0.2px;
  }

  .front-title {
    position: absolute;
    left: 634px;
    top: 92px;
    margin: 0;
    color: var(--saffron);
    font-weight: 500;
    font-size: 36px;
    line-height: 46px;
  }
  .front-author {
    position: absolute;
    left: 637px;
    top: 208px;
    margin: 0;
    color: var(--white);
    font-weight: 500;
    font-size: 21px;
  }

  .cord {
    position: absolute;
    height: 8px;
    background: var(--saffron);
  }
  .cord--left { left: 0; width: 851px; top: 435px; }
  .cord--right { left: 889px; right: 0; top: 441px; }
  .cord-knot {
    position: absolute;
    left: 850px;
    top: 398px;
    width: 40px;
    height: 90px;
    border-radius: 20px;
    background: var(--saffron);
  }
  .base-rule {
    position: absolute;
    left: 0;
    right: 0;
    top: 552px;
    height: 8px;
    background: var(--rule-dark);
  }
</style>
</head>
<body>
<div class="canvas">
  <div class="cover-spread">
    <div class="spine-fold spine-fold--left"></div>
    <div class="spine-fold spine-fold--right"></div>

    <section class="back-cover">
      <div class="publisher">
        <span class="publisher-mark"></span>
        <div class="publisher-name">Yunor Trenpa Publications</div>
      </div>
    </section>

    <div class="spine-title">A Window onto Stillness</div>

    <section class="front-cover">
      <h1 class="front-title">A Window<br>onto Stillness</h1>
      <p class="front-author">By Drawa Tsomen Lhundrup</p>
    </section>

    <div class="cord cord--left"></div>
    <div class="cord cord--right"></div>
    <div class="cord-knot" role="img" aria-label="Saffron looped knot ornament tied into the cord"></div>

    <div class="base-rule"></div>
  </div>
</div>
</body>
</html>
```